Redesign of existing Web Design Project

I wish to redsesign the web pages on www.bqrl.com.au

Background of Halvern Oakridge

Halvern Oakridge Construction Services was established in 2004 as a boutique construction company offering construction advice and management services. We assist people in the construction minefield – step by step.

We offer services in: -

• Construction Management
• Project Management
• Building

The essence of our business is ensuring every project we undertake achieves the client’s objectives. Our experience has shown the secrets to a profitable project are -

• Planning
• Attention to detail
• Value add

We take the trouble to understand the client’s needs in person. Our hands-on approach ensures those involved deliver to the required quality standards at the scheduled times.

Our area of works include: -

• Residential single and multistorey developments
• Education facilities
• Suburban commercial building and refurbishment
• Health
• Defence
• Industrial

Objective of Acquisition

We are planning to expand our business activities. We are aiming to increase our turnover and use website as an increased passive selling tool.

Possible company type

This is an ideal opportunity for person who can capture readers attention.

Target Market(s)

see www.bqrl.com.au

Industry/Entity Type

Construction

Requirements
Must have
• Capture peoples attention on readers zones

```html
<!DOCTYPE html>
<html lang="en">
<head>
<meta charset="utf-8">
<title>Halvern Oakridge Construction Services</title>
<link href="https://fonts.googleapis.com/css2?family=Inter:wght@400;500;600;700&display=swap" rel="stylesheet">
<style>
:root{
  --dark:#262b2f;
  --dark-line:#3b4146;
  --blue:#4a8fd6;
  --blue-deep:#2f6fb8;
  --sky:#8fbde8;
  --text:#222;
  --muted:#9aa0a5;
  --panel:#fbf9fa;
  --border:#dcdcdc;
}
*{box-sizing:border-box;margin:0;padding:0}
html,body{width:1088px;height:1200px;overflow:hidden}
body{font-family:"Inter",Arial,sans-serif;color:var(--text);background:#fff;position:relative}
.abs{position:absolute}
.header{left:0;top:0;width:1088px;height:94px;background:var(--dark)}
.datetime{right:145px;top:6px;color:#fff;font-size:11px;word-spacing:2px}
.brand{left:152px;top:28px;display:flex;align-items:center;gap:10px;color:#dfe6f0;font-size:21px;font-weight:500}
.brand .mark{width:26px;height:26px;background:#8fa6cf}
.phone{right:146px;top:38px;color:#d8d8d8;font-size:18px}
.phone b{font-weight:600}
.nav{left:142px;top:76px;width:803px;height:38px;background:linear-gradient(#5a9fe2,#3a7fc8);border-radius:3px;display:flex;z-index:2}
.nav a{color:#fff;text-decoration:none;font-size:13px;display:flex;align-items:center;justify-content:center;border-right:1px solid #2f6aae;height:100%}
.hero{left:0;top:94px;width:1088px;height:276px;background:linear-gradient(90deg,#cfd6dc 0%,#a9b9c9 35%,#7fa8d6 60%,var(--blue) 100%)}
.hero-photo{left:0;top:94px;width:660px;height:276px;background:linear-gradient(160deg,#8cb4df 0%,#b8b6ae 45%,#7d7a72 100%);-webkit-mask:linear-gradient(90deg,#000 75%,transparent)}
.hero h1{left:591px;top:164px;color:#fff;font-size:36px;font-weight:700}
.hero-sub{left:590px;top:214px;color:#fff;font-size:25px;font-weight:400}
.hero-btn{left:594px;top:256px;width:148px;height:37px;border:1px solid #fff;border-radius:3px;background:linear-gradient(#3e86d4,#2563ad);color:#fff;font-size:14px;display:flex;align-items:center;justify-content:center}
.welcome h2,.who{font-size:24px;font-weight:700}
.welcome{left:147px;top:394px;width:480px}
.welcome p{font-size:12px;line-height:18px;margin-top:10px;color:#333}
.who{left:147px;top:506px}
.uses{left:147px;top:545px;list-style:none;font-size:11.5px;color:#333}
.uses li{height:22.6px}
.gallery{left:657px;top:400px;width:281px;height:352px;background:var(--panel);border:1px solid var(--border);border-radius:3px}
.gallery h3{position:absolute;left:20px;top:14px;font-size:19px;font-weight:700}
.thumbs{position:absolute;left:20px;top:48px;display:grid;grid-template-columns:repeat(3,73px);column-gap:12px;row-gap:16px}
.thumbs span{height:48px;background:linear-gradient(135deg,#e7e3dc,#8a8f98 60%,#b04a3c)}
.thumbs span:nth-child(3n){background:linear-gradient(135deg,#d7cbb6,#6d5c49 60%,#c2532f)}
.gbtn{position:absolute;left:66px;top:306px;width:147px;height:31px;background:linear-gradient(#7c9ad6,#4f73be);color:#fff;font-size:13px;display:flex;align-items:center;justify-content:center;border-radius:2px}
.carousel{left:136px;top:758px;width:803px;height:107px;border:1px solid var(--border);border-radius:3px;background:#fff}
.slide{top:14px;width:138px;height:80px;background:linear-gradient(#5a8bd0,#c8d6e4 60%,#7f8c76)}
.arrow{top:38px}
.footer{left:0;top:879px;width:1088px;height:321px;background:var(--dark)}
.testi-title{left:151px;top:896px;color:var(--muted);font-size:18px;font-weight:600}
.testi{top:930px;color:var(--muted);font-size:11.5px;line-height:22.6px;width:250px}
.testi b{font-weight:600}
.download{left:721px;top:909px;width:215px;height:71px;border:1px solid var(--dark-line);border-radius:3px}
.download .ico{position:absolute;left:8px;top:14px;width:44px;height:44px}
.download strong{position:absolute;left:66px;top:12px;color:#fff;font-size:24px;font-weight:600}
.download small{position:absolute;left:66px;top:42px;color:#fff;font-size:13px;font-weight:600}
.hr{left:0;width:1088px;height:1px;background:var(--dark-line)}
.fnav{left:0;top:1050px;width:1088px;text-align:center;color:var(--muted);font-size:12px;word-spacing:1px}
.fnav i{font-style:normal;margin:0 11px}
.vchat{left:152px;top:1100px;width:50px;height:42px;border-radius:50%;background:#1b1f22;border:2px solid #4a5055}
.vtext{left:217px;top:1109px;color:#d9d9d9;font-size:19px}
.soc{top:1096px;width:49px;height:49px;border-radius:8px;background:#5c6166;color:#eee;font-size:9px;display:flex;align-items:center;justify-content:center;text-align:center}
.vdiv{left:500px;top:1083px;width:1px;height:74px;background:var(--dark-line)}
.copy{left:0;top:1171px;width:1088px;text-align:center;color:var(--muted);font-size:10px}
.copy i{font-style:normal;margin:0 9px}
</style>
</head>
<body>
<header class="abs header"></header>
<div class="abs datetime">Saturday 14 jan 2012 &nbsp; 12.10 pm</div>
<div class="abs brand"><span class="mark"></span>Halvern Oakridge Construction Services</div>
<div class="abs phone"><b>Phone</b> : &nbsp;+61 2 5550 3148</div>
<nav class="abs nav">
  <a style="width:81px">Home</a><a style="width:95px">About Us</a><a style="width:89px">Building</a><a style="width:194px">Construction Management</a><a style="width:167px">Project Management</a><a style="width:177px;border:0">Contacts</a>
</nav>

<section class="abs hero"></section>
<div class="abs hero-photo" role="img" aria-label="Photo of a multistorey concrete building under construction with a tower crane"></div>
<div class="hero"><h1 class="abs">Deliver the project</h1>
<div class="abs hero-sub">you want on time, To budget</div>
<div class="abs hero-btn">View our projects</div></div>

<section class="abs welcome">
  <h2>Welcome to Halvern Oakridge</h2>
  <p>We are a Sydney based Construction Company who can help with all your construction needs. The Halvern Oakridge process helps define your budget, establishes Return on Investment and reduces potential risk.</p>
</section>
<h2 class="abs who">Who uses us?</h2>
<ul class="abs uses">
  <li>Architects – to assist with costing a project, value-engineering and project implementation.</li>
  <li>Owner/Builders – to assist with project management, costings, work flow and final sign offs</li>
  <li>Developers – to assist with costings, tender appraisal and project management</li>
  <li>Strata managers – remediation, fire safety</li>
  <li>Sub-contractors – for pricing assistance</li>
  <li>Lessor and lessees – for fit outs and make good work</li>
  <li>Investors – to define profitability, feasibility and risk</li>
  <li>Finance companies – risk analysis</li>
  <li>Solicitors – advisory services</li>
</ul>

<aside class="abs gallery">
  <h3>Project Gallery</h3>
  <div class="thumbs" role="img" aria-label="Thumbnails of finished interiors: dining rooms and staircases">
    <span></span><span></span><span></span><span></span><span></span><span></span>
    <span></span><span></span><span></span><span></span><span></span><span></span>
  </div>
  <div class="gbtn">View all projects</div>
</aside>

<section class="abs carousel">
  <svg class="abs arrow" style="left:10px" width="14" height="26"><path d="M11 2 3 13l8 11" fill="none" stroke="#888" stroke-width="3"/></svg>
  <div class="abs slide" style="left:31px" role="img" aria-label="Glass-fronted office building"></div>
  <div class="abs slide" style="left:182px;background:linear-gradient(#6c6f78,#3a3028 60%,#8a6a3c)" role="img" aria-label="Modern building lit at dusk"></div>
  <div class="abs slide" style="left:334px;background:linear-gradient(#7aa4d8,#e0d6b8 50%,#6d8050)" role="img" aria-label="Multistorey residential house"></div>
  <div class="abs slide" style="left:482px;background:linear-gradient(#1d4fb0,#e8ecf2 55%,#9aa7b5)" role="img" aria-label="White commercial building under blue sky"></div>
  <div class="abs slide" style="left:631px;background:linear-gradient(#3f6fc0,#dfe6ee 50%,#6e8a5a)" role="img" aria-label="Office building with curved glass facade"></div>
  <svg class="abs arrow" style="left:778px" width="14" height="26"><path d="M3 2l8 11-8 11" fill="none" stroke="#888" stroke-width="3"/></svg>
</section>

<footer class="abs footer"></footer>
<h3 class="abs testi-title">Testimonials</h3>
<p class="abs testi" style="left:153px">Halvern Oakridge is a construction company with significant skills in Project and Construction Management. We will help you undertake a successful construction.</p>
<p class="abs testi" style="left:429px;width:240px">“The success of our Newcastle project built our confidence in the ability of Halvern Oakridge.”<br><b>Dana Whitfield</b><br><b>Director Corvale Constructions</b></p>
<div class="abs download">
  <svg class="ico" viewBox="0 0 44 44"><rect x="8" y="4" width="30" height="30" rx="3" fill="#4a8fd6" transform="rotate(-12 23 19)"/><path d="M10 22h8v-8h6v8h8L21 36z" fill="#f08a1c"/></svg>
  <strong>Download</strong><small>Corporate Brochure</small>
</div>
<div class="abs hr" style="top:1035px"></div>
<nav class="abs fnav">Home<i>|</i>About Us<i>|</i>Building<i>|</i>Construction Management<i>|</i>Project Management<i>|</i>Links<i>|</i>Free Downloads<i>|</i>Careers<i>|</i>Contacts</nav>
<div class="abs hr" style="top:1082px"></div>
<div class="abs vchat"><svg width="46" height="38" viewBox="0 0 46 38"><rect x="12" y="13" width="14" height="12" rx="2" fill="#fff"/><path d="M27 17l7-4v12l-7-4z" fill="#fff"/></svg></div>
<div class="abs vtext">Live video Chat</div>
<div class="abs soc" style="left:381px;border-radius:50%">Vidlink</div>
<div class="abs vdiv"></div>
<div class="abs soc" style="left:567px">Friendnet</div>
<div class="abs soc" style="left:638px">Callwave</div>
<div class="abs soc" style="left:712px">Worklink</div>
<div class="abs soc" style="left:793px;top:1101px;width:71px;height:38px;background:#eee;color:#333;border-radius:3px;font-size:11px">Plusone</div>
<div class="abs hr" style="top:1157px"></div>
<div class="abs copy">Copyright © 2008 Halvern Oakridge, All Rights Reserved - Webmaster<i>|</i>Privacy policy<i>|</i>Admin</div>
</body>
</html>
```